Hold Each Morning As A MOSSbright Harbour

Hello Designers! We need a captivating notebook cover design for our self-development company for people with disabilities. We help people with a diagnosis see everyday as a great adventure than something to ensure. This notebook is to capture the brightness and positivity of everyday, that your struggles are meant for you to overcome. We would like to see designs that follow with our brand (uploaded) and I've also added our logo and kind of notebook as a guide. The final design should be inviting and bright. Use the title "Keep Each Morning A Quiet Lantern". Will decide the words once the background design is finalized

Notebook Size: 8.5 x 5.75 inches
Updates

Hello Designers! I'm extending the deadline to give you an opportunity to submit different and unique designs for the MOSSbright HARBOUR Journal. I've given feedback to most of you so this is your opportunity to try something new. Looking for clean, inviting and unique designs that use the logo colour scheme (attached -- navy blue, light blue, yellow, black). Preferably front and back cover designs.

Target Market(s)

Between 25-35 years

Font styles to use
Serif
Sans Serif
Decorative
Script

Colors
0255a3
fbed22

Requirements
Must have
• -Use colour scheme as per attachment as main colours (can go beyond for contrast ex. pinks/purples/indigo/etc)
Nice to have
• Would like to see designs related to nature, art and/or graphic prints.
Should not have
• icons (no stick figures), silhouettes of people, no hands
• NO stock images

```html
<!DOCTYPE html>
<html lang="en">
<head>
<meta charset="utf-8">
<title>MOSSbright Harbour Journal Cover</title>
<link rel="stylesheet" href="https://fonts.googleapis.com/css2?family=Amatic+SC:wght@400;700&display=swap">
<style>
  :root {
    --page-bg: #ffffff;
    --cover-yellow: #f8ea24;
    --sun-glow: #fbf08a;
    --ink-blue: #1a5bb5;
    --ridge-peach: #f3b483;
    --ridge-coral: #ee7a52;
    --ridge-rose: #c4476a;
    --ridge-plum: #6a1470;
  }
  * { margin: 0; padding: 0; box-sizing: border-box; }
  html, body {
    width: 1200px;
    height: 1200px;
    overflow: hidden;
    background: var(--page-bg);
  }
  .stage {
    position: relative;
    width: 1200px;
    height: 1200px;
  }
  .cover {
    position: absolute;
    left: 234px;
    top: 53px;
    width: 724px;
    height: 1070px;
    background: var(--cover-yellow);
    overflow: hidden;
    box-shadow: 0 2px 6px rgba(0, 0, 0, 0.18);
  }
  .brand {
    position: absolute;
    right: 34px;
    top: 40px;
    display: flex;
    align-items: center;
    gap: 10px;
    color: var(--ink-blue);
    font-family: "Amatic SC", sans-serif;
    font-weight: 700;
    line-height: 0.95;
    text-align: right;
    z-index: 2;
  }
  .brand-dot {
    width: 12px;
    height: 12px;
    border-radius: 50%;
    background: var(--ink-blue);
  }
  .brand-name { font-size: 34px; display: block; }
  .brand-tag { font-size: 17px; display: block; letter-spacing: 1px; }
  .sun {
    position: absolute;
    left: 84px;
    top: 313px;
    width: 516px;
    height: 516px;
    border-radius: 50%;
    background: radial-gradient(circle, var(--sun-glow) 0%, var(--sun-glow) 86%, rgba(251, 240, 138, 0) 100%);
    opacity: 0.85;
  }
  .ridges {
    position: absolute;
    left: 0;
    top: 760px;
    width: 724px;
    height: 310px;
    background: linear-gradient(to bottom,
      rgba(243, 180, 131, 0) 0%,
      var(--ridge-peach) 16%,
      var(--ridge-coral) 42%,
      var(--ridge-rose) 70%,
      var(--ridge-plum) 100%);
  }
  .headline {
    position: absolute;
    left: 160px;
    top: 416px;
    color: var(--ink-blue);
    font-family: "Amatic SC", sans-serif;
    font-weight: 400;
    text-transform: uppercase;
    white-space: nowrap;
    z-index: 2;
  }
  .headline-lead {
    display: block;
    font-size: 66px;
    line-height: 68px;
    letter-spacing: 2px;
  }
  .headline-main {
    display: block;
    font-size: 140px;
    line-height: 114px;
    letter-spacing: 10px;
  }
  .headline-lead + .headline-main { margin-top: 9px; }
</style>
</head>
<body>
<div class="stage">
  <main class="cover">
    <div class="brand">
      <span>
        <span class="brand-name">Rena's</span>
        <span class="brand-tag">MOSSBRIGHT HARBOUR</span>
      </span>
      <span class="brand-dot"></span>
    </div>

    <div class="sun"></div>

    <div class="ridges" role="img" aria-label="Layered contour mountain range in peach, coral, rose and plum tones"></div>

    <h1 class="headline">
      <span class="headline-lead">Keep</span>
      <span class="headline-lead">Each Morning</span>
      <span class="headline-main">A Quiet</span>
      <span class="headline-main">Lantern</span>
    </h1>
  </main>
</div>
</body>
</html>
```